Design a New Site for a very cool Watch

We have the overall design element of the website and the banners in the PSD file. We need someone to finish our design in PSD and than convert to HTML. We have included the instructions, PSD file, images and all text.

We currently use Hubspot to host and make changes to our site. The entire design aspect is complete so all we need is some minor changes and additions within the photoshop design and than the coding into HTML.

Please only sign up if you understand photoshop and HTML conversion

Here is the DropBox link to the files
https://files.quorvel-share.net/s/pm4kx82lwq7dtne/Belthor%20Site.zip
Updates

We have the basic design concept in Photoshop.  We just need someone who can complete some changes, make some additions and convert to HTML

Target Market(s)

Watch Buyers

Requirements
Must have
• Must look like a professional luxury brand

Our brand colors are very basic with Black, White and Grey can be used

```html
<!DOCTYPE html>
<html lang="en">
<head>
<meta charset="utf-8">
<title>Belthor &amp; Co.</title>
<link rel="stylesheet" href="https://fonts.googleapis.com/css2?family=Open+Sans:wght@400;600&family=Arimo:wght@400&display=swap">
<style>
:root{
  --ink:#2d2d2d;
  --bar:#2f2f2f;
  --footer:#2b2b2b;
  --grey:#a9a9a9;
  --soft:#fdf8f8;
  --card:#fdf0f0;
  --card-line:#e6d9d9;
  --icon:#777;
  --social:#bdbdbd;
  --red:#d8181e;
  --white:#fff;
  --dash:#d8d8d8;
}
*{box-sizing:border-box;margin:0;padding:0}
html,body{width:1024px;height:1200px;overflow:hidden;background:var(--white)}
body{position:relative;font-family:"Open Sans",sans-serif;color:var(--ink)}
.abs{position:absolute}
.top-rule{left:0;top:0;width:1024px;height:5px;background:var(--bar)}
.utility{top:12px;left:82px;font-size:10px;display:flex;gap:18px}
.utility-right{top:12px;right:82px;font-size:10px;display:flex;gap:10px;align-items:center}
.utility-right .shop{color:var(--red)}
.utility-right .sep{width:1px;height:12px;background:#aaa}
.utility-right .auth{font-family:"Arimo",sans-serif}
.brand{top:48px;left:0;width:1024px;text-align:center;font-size:19px;letter-spacing:.5px;display:flex;justify-content:center;align-items:center;gap:10px}
.brand .mark{width:20px;height:20px;border:2px solid var(--ink)}
.dash{left:0;width:1024px;border-top:1px dashed var(--dash)}
.nav{top:113px;left:0;width:1024px;height:29px;background:var(--bar)}
.nav ul{list-style:none;display:flex;position:absolute;left:84px;top:0;height:29px;align-items:center}
.nav li{font-family:"Arimo",sans-serif;font-size:10px;color:var(--white);margin-right:26px;display:flex;align-items:center;gap:10px}
.nav li span{font-size:12px;font-weight:700}
.nav .search{position:absolute;left:741px;top:0;width:209px;height:29px;background:#4a4a4a;display:flex}
.nav .search span{flex:1;font-family:"Arimo",sans-serif;font-size:10px;color:#999;padding:9px 12px}
.nav .search b{width:31px;height:29px;background:#1e1e1e;display:flex;align-items:center;justify-content:center}
.hero{top:173px;left:0;width:1024px;height:322px;background:linear-gradient(120deg,#1f2f5c 0%,#34374a 30%,#252a36 55%,#0d0e12 75%,#000 100%)}
.hero-band{top:495px;left:0;width:1024px;height:7px;background:#777}
.arrow-btn{width:40px;height:40px;background:#222;color:#ddd;font-size:13px;display:flex;align-items:center;justify-content:center;top:136px}
.callout{left:697px;width:252px;background:linear-gradient(#ddd,#aaa);border:2px solid #8c8c8c;display:flex;align-items:center;gap:10px;padding:6px 10px;font-size:11.5px;font-weight:600;line-height:15px;color:#222}
.callout .gem{width:56px;height:56px;border-radius:50%;flex:none}
.dots{top:300px;left:442px;display:flex;gap:6px}
.dots i{width:9px;height:9px;border-radius:50%;background:#888}
.dots i.on{background:var(--white)}
.soft{top:770px;left:0;width:1024px;height:325px;background:var(--soft)}
.card{top:551px;width:203px;height:232px;background:var(--card);border:1px solid var(--card-line);text-align:center;font-size:11.5px;line-height:17px;letter-spacing:.2px}
.card::after{content:"";position:absolute;left:-1px;right:-1px;bottom:-1px;height:7px;background:var(--grey)}
.card .disc{width:96px;height:96px;border-radius:50%;background:var(--white);border:1px solid #ddd;margin:35px auto 31px;display:flex;align-items:center;justify-content:center}
.rule{top:829px;left:0;width:1024px;border-top:1px solid #e8e0e0}
.about-title{top:852px;left:73px;font-size:13px;font-weight:400;letter-spacing:.5px}
.about-photo{top:888px;left:73px;width:203px;height:102px;background:linear-gradient(90deg,#6b5a4c,#3a3330 55%,#5d4a3c)}
.about-text{top:893px;left:298px;width:190px;font-family:"Arimo",sans-serif;font-size:9.4px;line-height:13.7px;color:#555}
.about-text a{color:var(--red);text-decoration:none;display:block}
.touch{top:884px;left:540px;width:170px;text-align:center}
.touch h3{font-size:17px;font-weight:600;color:#444;margin-top:6px}
.social{top:935px;left:746px;width:194px;height:37px;background:#ececec;display:flex;align-items:center;justify-content:space-around;padding:0 6px}
.bar-grey{top:1032px;height:7px;background:var(--grey)}
.footer{top:1111px;left:0;width:1024px;height:89px;background:var(--footer);color:var(--white)}
.footer ul{list-style:none;display:flex;justify-content:center;gap:27px;margin-top:32px;font-family:"Arimo",sans-serif;font-size:9.6px;letter-spacing:.3px}
.footer p{text-align:center;font-family:"Arimo",sans-serif;font-size:9px;color:#ccc;margin-top:14px}
</style>
</head>
<body>
<div class="abs top-rule"></div>
<nav class="abs utility"><span>My Account</span><span>Collection</span><span>Lifestyle</span><span>Shop now</span></nav>
<div class="abs utility-right"><span class="shop">shop.belthor.com</span><span class="sep"></span><span class="auth">Sign in - Register</span></div>
<div class="abs brand"><span class="mark"></span><span>BELTHOR &amp; CO.</span></div>
<div class="abs dash" style="top:97px"></div>

<div class="abs nav">
  <ul>
    <li>HOME</li>
    <li>PRODUCTS <span>&#8250;</span></li>
    <li>ARTICLES <span>&#8250;</span></li>
    <li>PHOTO GALLERY <span>&#8250;</span></li>
    <li>BLOG</li>
    <li>CONTACT</li>
  </ul>
  <div class="search"><span>SEARCH</span><b><svg width="16" height="16" viewBox="0 0 16 16"><circle cx="6" cy="6" r="4.2" fill="none" stroke="#fff" stroke-width="2"/><line x1="9" y1="9" x2="14" y2="14" stroke="#fff" stroke-width="2.4"/></svg></b></div>
</div>
<div class="abs dash" style="top:156px"></div>

<section class="abs hero" role="img" aria-label="Close-up of a square watch face with floating diamonds and a moon-stone dome">
  <svg class="abs" style="left:0;top:0" width="1024" height="322">
    <circle class="dome" cx="430" cy="185" r="33" fill="#2a2d38" stroke="#6a6e7c" stroke-width="2"/>
    <circle class="diamond-point" cx="425" cy="113" r="5" fill="none" stroke="#d8dbe4" stroke-width="2"/>
    <line x1="430" y1="113" x2="700" y2="95" stroke="var(--red)" stroke-width="2"/>
    <circle cx="445" cy="205" r="3" fill="var(--red)"/>
    <line x1="445" y1="205" x2="712" y2="250" stroke="var(--red)" stroke-width="2"/>
  </svg>
  <div class="abs arrow-btn" style="left:57px">&#8249;</div>
  <div class="abs arrow-btn" style="left:927px">&#8250;</div>
  <div class="abs callout" style="top:53px;height:82px"><span class="gem" style="background:radial-gradient(#8a8fa8,#1c1e2a)"></span><span>70 Free floating diamonds suspended in a special clear liquid</span></div>
  <div class="abs callout" style="top:208px;height:82px"><span class="gem" style="background:radial-gradient(#6e6e78,#1a1a22)"></span><span>Authenticated piece of the Moon, Mars and a rare space gem underneath the dome</span></div>
  <div class="abs dots"><i></i><i></i><i></i><i></i><i class="on"></i></div>
</section>
<div class="abs hero-band"></div>

<div class="abs soft"></div>

<article class="abs card" style="left:73px">
  <div class="disc"><svg width="56" height="56" viewBox="0 0 56 56" fill="var(--icon)"><polygon points="30,18 35,30 48,31 38,39 41,52 30,45 19,52 22,39 12,31 25,30"/><polygon points="14,4 17,11 24,12 19,16 20,23 14,19 8,23 9,16 4,12 11,11"/><polygon points="42,10 44,15 49,15 45,18 46,23 42,20 38,23 39,18 35,15 40,15"/></svg></div>
  THE ORION STORY
</article>
<article class="abs card" style="left:298px">
  <div class="disc"><svg width="62" height="44" viewBox="0 0 62 44"><rect x="9" y="2" width="44" height="30" rx="3" fill="var(--icon)"/><rect x="13" y="6" width="36" height="22" fill="#eee"/><text x="31" y="20" font-family="Arimo,sans-serif" font-size="6.5" text-anchor="middle" fill="#666">REGISTER</text><path d="M2 35h58l-4 7H6z" fill="var(--icon)"/></svg></div>
  REGISTER YOUR<br>WATCH
</article>
<article class="abs card" style="left:523px">
  <div class="disc"><svg width="64" height="56" viewBox="0 0 64 56" fill="none" stroke="var(--icon)" stroke-width="3"><rect x="14" y="2" width="12" height="10" rx="2"/><rect x="14" y="44" width="12" height="10" rx="2"/><circle cx="20" cy="28" r="15"/><line x1="20" y1="28" x2="20" y2="18"/><line x1="20" y1="28" x2="27" y2="32"/><circle cx="48" cy="18" r="6" stroke-width="5" stroke-dasharray="3 2"/><circle cx="50" cy="40" r="5" stroke-width="4" stroke-dasharray="3 2"/></svg></div>
  REPAIR, MAINTENANCE<br>&amp; WARRENTY INFO
</article>
<article class="abs card" style="left:748px">
  <div class="disc"><svg width="70" height="40" viewBox="0 0 70 40"><path d="M16 4l52 8-4 24-54-8L2 14z" fill="var(--icon)"/><circle cx="12" cy="16" r="3" fill="#fff"/><text x="40" y="25" font-family="Open Sans,sans-serif" font-size="13" font-weight="600" fill="#fff" text-anchor="middle" transform="rotate(8 40 22)">New</text></svg></div>
  REGISTER TO FIND OUT ABOUT<br>NEW WATCH COLECTIONS
</article>

<div class="abs rule"></div>
<h2 class="abs about-title">BELTHOR &amp; CO</h2>
<div class="abs about-photo" role="img" aria-label="Woman standing beside a watch campaign poster"></div>
<p class="abs about-text">Lorem ipsum dolor sit amet, consectetur adipisicing elit, sed do eiusmod tempor incididunt ut labore et dolore magna aliqua. Ut enim ad minim veniam, quis nostrud exercitation ullamco laboris nisi ut aliquip ex ea commodo consequat. <a href="#">www.belthor.com</a></p>
<div class="abs touch">
  <svg width="80" height="62" viewBox="0 0 80 62"><path d="M14 30a26 22 0 0 0 52 0" fill="none" stroke="#666" stroke-width="6"/><rect x="27" y="14" width="26" height="18" fill="#666"/><path d="M27 14l13 10 13-10" fill="none" stroke="#fff" stroke-width="2"/><rect x="32" y="4" width="16" height="10" fill="#666"/></svg>
  <h3>KEEP IN TOUCH</h3>
</div>
<div class="abs social" aria-label="Follow and share links">
  <svg width="26" height="26" viewBox="0 0 26 26" aria-label="Share"><g fill="var(--social)"><circle cx="19" cy="5" r="4"/><circle cx="6" cy="13" r="4"/><circle cx="19" cy="21" r="4"/></g><path d="M19 5L6 13l13 8" fill="none" stroke="var(--social)" stroke-width="2.5"/></svg>
  <svg width="26" height="26" viewBox="0 0 26 26" aria-label="Message"><path d="M2 4h22v14H10l-6 5v-5H2z" fill="var(--social)"/></svg>
  <svg width="26" height="26" viewBox="0 0 26 26" aria-label="Favourite"><path d="M13 23L3 13a5.5 5.5 0 0 1 10-7 5.5 5.5 0 0 1 10 7z" fill="var(--social)"/></svg>
  <svg width="26" height="26" viewBox="0 0 26 26" aria-label="Link"><g fill="none" stroke="var(--social)" stroke-width="3.5"><rect x="2" y="9" width="13" height="8" rx="4"/><rect x="11" y="9" width="13" height="8" rx="4"/></g></svg>
  <svg width="26" height="26" viewBox="0 0 26 26" aria-label="Email"><rect x="2" y="5" width="22" height="16" fill="var(--social)"/><path d="M2 5l11 9 11-9" fill="none" stroke="#ececec" stroke-width="2"/></svg>
</div>
<div class="abs bar-grey" style="left:73px;width:427px"></div>
<div class="abs bar-grey" style="left:524px;width:427px"></div>
<div class="abs dash" style="top:1095px"></div>

<footer class="abs footer">
  <ul><li>BELTHOR &amp; COMPANY</li><li>CONTACT US</li><li>TERMS OF SERVICE</li><li>REFUND POLICY</li><li>PRIVACY POLICY</li></ul>
  <p>Copyright &copy; 2013 Belthor &amp; Co<sup>TM</sup></p>
</footer>
</body>
</html>
```